Flyer PRTW

Everyone deserves true happiness.
Real Food is the answer to:
A body you love
Reverting illnesses
Healthy digestion
Stable blood sugar
Emotions in control
Blasting energy
Sound sleep
REAL food + water + exercise + Laughter =
“HIGH QUALITY OF LIFE “
EASY, right?
Challenging: certainly
Changing habits: reluctance in sight!
WE’RE OFFER TO:
1. Study YOUR unique body composition, food cravings, blockages, illnesses, and personality!
2. Introduce you to new Food
3. customized wellness plan with follow ups
4. meditation,cooking, and fitness classes as well as wellness workshops
5. New friends with high aspirations
LOGO
Contact info
Please visit our web address to see our design style and colors: www.pinerivertallwave.net
Target Market(s)
people who want to be more healthy
Industry/Entity Type
Fitness
Requirements
Must have
- beautiful pictures of fresh food (main picture) and maybe a few more small pictures reflecting
exercise
healthy living
meditation
Nice to have
- look is crucial. recall some of the color or colors from my logo to have a theme

```html
<!DOCTYPE html>
<html lang="en">
<head>
<meta charset="utf-8">
<title>PRTW Flyer – High Quality of Life Easy</title>
<link rel="stylesheet" href="https://fonts.googleapis.com/css2?family=Carlito:ital,wght@0,400;0,700;1,700&family=Luckiest+Guy&family=Arimo:wght@700&display=swap">
<style>
  :root {
    --band-yellow: #f7c53c;
    --band-yellow-light: #fbd96a;
    --green-light: #d4eba6;
    --green-mid: #a9d46f;
    --green-deep: #7fbd4a;
    --leaf-tint: rgba(235, 247, 205, 0.45);
    --title-green: #9ccc2c;
    --title-edge: #ffffff;
    --ink: #1c1c1c;
    --accent-orange: #e8a21c;
    --brand-green: #5aa32a;
    --photo-frame: #ffffff;
  }
  * { box-sizing: border-box; margin: 0; padding: 0; }
  html, body { width: 1200px; height: 933px; overflow: hidden; background: #ffffff; }

  .flyer {
    position: relative;
    width: 1200px;
    height: 933px;
    overflow: hidden;
    background:
      radial-gradient(ellipse 70% 75% at 45% 50%, var(--green-light) 0%, var(--green-mid) 70%, var(--green-deep) 100%);
    font-family: "Carlito", "Calibri", sans-serif;
    color: var(--ink);
  }

  .leaf-pattern {
    position: absolute;
    left: 520px;
    top: 70px;
    width: 680px;
    height: 796px;
    background:
      radial-gradient(ellipse 28% 22% at 78% 78%, var(--leaf-tint) 0%, transparent 100%),
      radial-gradient(ellipse 22% 30% at 62% 45%, var(--leaf-tint) 0%, transparent 100%),
      radial-gradient(ellipse 30% 20% at 40% 18%, var(--leaf-tint) 0%, transparent 100%),
      radial-gradient(ellipse 18% 26% at 92% 30%, var(--leaf-tint) 0%, transparent 100%);
  }

  .band {
    position: absolute;
    left: 0;
    width: 100%;
    background: linear-gradient(180deg, var(--band-yellow-light), var(--band-yellow));
  }
  .band--top { top: 0; height: 70px; }
  .band--bottom { bottom: 0; height: 67px; }

  .headline {
    position: absolute;
    left: 44px;
    top: 104px;
    font-family: "Luckiest Guy", "Arial Black", sans-serif;
    font-weight: 400;
    font-size: 46px;
    line-height: 54px;
    letter-spacing: 1px;
    color: var(--title-green);
    -webkit-text-stroke: 2px var(--title-edge);
    paint-order: stroke fill;
    text-shadow: 2px 3px 3px rgba(40, 80, 10, 0.45);
    transform: skewX(-8deg);
    white-space: nowrap;
  }

  .formula {
    position: absolute;
    left: 20px;
    top: 204px;
    width: 366px;
    text-align: center;
    font-size: 19px;
    line-height: 24px;
  }
  .challenge {
    position: absolute;
    left: 20px;
    top: 356px;
    width: 366px;
    text-align: center;
    font-size: 21px;
    line-height: 30px;
    font-style: italic;
    font-weight: 700;
  }

  .approach {
    position: absolute;
    left: 425px;
    top: 210px;
    width: 350px;
    text-align: center;
    font-size: 16.5px;
    line-height: 24.5px;
  }
  .approach p + p { margin-top: 24px; }

  .photo {
    position: absolute;
    border: 6px solid var(--photo-frame);
    box-shadow: 2px 4px 10px rgba(0, 0, 0, 0.35);
  }
  .photo--produce {
    left: 820px;
    top: 121px;
    width: 318px;
    height: 220px;
    transform: rotate(-6deg);
    background: linear-gradient(135deg, #5c8a34 0%, #d9772a 50%, #3a3a2a 100%);
  }
  .photo--treadmill {
    left: 33px;
    top: 455px;
    width: 278px;
    height: 182px;
    background: linear-gradient(135deg, #4a3526 0%, #9a7050 100%);
  }
  .photo--jump {
    left: 113px;
    top: 619px;
    width: 280px;
    height: 193px;
    background: linear-gradient(180deg, #6ea6dd 0%, #c4dcf0 100%);
  }

  .brand {
    position: absolute;
    left: 808px;
    top: 428px;
    display: flex;
    align-items: center;
    gap: 12px;
  }
  .brand__dot {
    width: 84px;
    height: 84px;
    border-radius: 50%;
    background: var(--brand-green);
    flex: none;
  }
  .brand__name {
    font-family: "Carlito", "Calibri", sans-serif;
    font-weight: 400;
    font-size: 31px;
    color: var(--brand-green);
    white-space: nowrap;
  }

  .join {
    position: absolute;
    left: 410px;
    top: 508px;
    width: 400px;
    text-align: center;
    font-family: "Arimo", "Arial", sans-serif;
    font-weight: 700;
    font-size: 22px;
    line-height: 33px;
  }
  .join__tag { color: var(--accent-orange); }

  .contact {
    position: absolute;
    left: 410px;
    top: 611px;
    width: 400px;
    text-align: center;
    font-family: "Arimo", "Arial", sans-serif;
    font-weight: 700;
  }
  .contact__label { font-size: 20px; line-height: 26px; }
  .contact__phone { font-size: 20px; line-height: 26px; }
  .contact__web { font-size: 16px; line-height: 26px; margin-top: 2px; }
</style>
</head>
<body>
  <main class="flyer">
    <div class="leaf-pattern" role="img" aria-label="Faint pattern of large pale leaves and curling stems across the background"></div>

    <div class="band band--top"></div>

    <h1 class="headline">HIGH QUALITY OF LIFE EASY</h1>

    <p class="formula">With real food + water + exercise + L.O.L.<br>We believe this wil equal a<br>“High Quality of Life”</p>

    <p class="challenge">Challenging: Certainly<br>Changing habits: Reluctance &nbsp;in sight!</p>

    <div class="approach">
      <p>Most approaches to nutrition dwell on calories, carbs, fats, proteins. Instead of creating lists of re-strictions and good and bad foods, I coach my clients to create a happy, healthy life in a way that is flexible, fun and free of denial and discipline.</p>
      <p>I will guide you to find the food and lifestyle choices that best support you. I will also help you to make gradual, lifelong changes that enable you to reach your current and future health goals.</p>
    </div>

    <div class="photo photo--produce" role="img" aria-label="Photo of fresh vegetables: peppers, corn, broccoli, cabbage and an orange"></div>
    <div class="photo photo--treadmill" role="img" aria-label="Photo of a person running on a treadmill in a gym"></div>
    <div class="photo photo--jump" role="img" aria-label="Photo of a woman leaping joyfully against a blue sky over a grassy field"></div>

    <div class="brand">
      <span class="brand__dot"></span>
      <span class="brand__name">Pine River Tallwave</span>
    </div>

    <p class="join">Join Our<br><span class="join__tag">PRTW</span> Community - It's Free!</p>

    <div class="contact">
      <p class="contact__label">Contact</p>
      <p class="contact__phone">Phone: (555) 014-2290</p>
      <p class="contact__web">http://www.pinerivertallwave.net/</p>
    </div>

    <div class="band band--bottom"></div>
  </main>
</body>
</html>
```